Women's Health - Hormone Imbalance, Menopause, Perimenopause.

We need a poster to match a letter that will be sent out. So people see the poster in store they are reminded about the letter and the newspaper ad.
The Poster is advertising a holistic approach to treating menopause, perimenopause and women's health in general specifically hormonal imbalance.
This it the writing required on the poster
"Are you feeling out of sorts? Is your body changing? Could it be your hormones?
If you’re experiencing changes due to hormonal imbalances, it’s important to consult with a qualified medical professional who understands your needs.
Karim Oduya, the vBlendwell Apothecary, can help. He has practiced pharmacy and nutritional medicine, helping people with hormone imbalances using a holistic approach for over 18 years.
Together, we look at issues around Hormonal Imbalance, Perimenopause and Menopause. To start, we take a profile of your sex hormones, Adrenals, Thyroids and Metabolic Pathways to see how we can best remedy the situation. Karim uses a holistic approach that treats you as a whole – not just the symptoms – for overall better wellness.
Want to know more? Karim is available for consultation on Wednesday Mornings at Fern Gully Pharmacy and Thursday Mornings at Cape Lorne Pharmacy.
SPECIAL OFFER! Make a booking for one session ($60) and get another session free! This limited-time package includes an initial consultation, historical hormone profile, follow-up consultation and wellness action plan.
To book an appointment with Karim, call 1300 482 615 today."
Pictures required to correspond with the writing. I've also uploaded my logo
Pharmacy
Requirements
Must have
- Photos/Images to match the writing. Need women who are suffering from menopause with symptoms such as hot flashes, night sweats, anxiety, depression, fatigue, loss of libido, insomnia.
Nice to have
- Integrative Medicine, tailored medicine approach, Natural, approach, unique, tailor made solution

```html
<!DOCTYPE html>
<html lang="en">
<head>
<meta charset="utf-8">
<title>Hormone Health Poster</title>
<link rel="stylesheet" href="https://fonts.googleapis.com/css2?family=Roboto+Slab:wght@800&family=Fira+Sans+Condensed:wght@300;400;600;700&family=Open+Sans:wght@400;600;700&display=swap">
<style>
:root{
  --page:#e9e9ea;
  --paper:#ffffff;
  --orange:#f0a01e;
  --slate:#363d48;
  --card-head:#3e444d;
  --red:#a81c22;
  --red-deep:#8e171c;
  --yellow:#f5e21a;
  --band-yellow:#e9e51f;
  --navy-band:#0e4a6c;
  --navy-text:#1b2f6b;
  --green:#a9c43a;
  --ink:#1a1a1a;
  --black:#0c0c0c;
  --white:#ffffff;
}
*{box-sizing:border-box;margin:0;padding:0}
html,body{width:1200px;height:1200px;overflow:hidden;background:var(--page)}
.canvas{position:relative;width:1200px;height:1200px}
.poster{
  position:absolute;left:187px;top:21px;width:712px;height:998px;
  background:var(--paper);transform:scale(1.16);transform-origin:0 0;
  font-family:"Fira Sans Condensed",sans-serif;color:var(--white);
  box-shadow:0 6px 24px rgba(0,0,0,.18);overflow:hidden;
}
.abs{position:absolute}
.headline-bubble{left:0;top:0;width:712px;height:130px}
.headline{
  left:26px;top:31px;width:660px;height:74px;display:flex;align-items:center;justify-content:center;
  font-family:"Roboto Slab",serif;font-weight:800;font-size:38px;letter-spacing:-1px;
  color:var(--white);text-shadow:0 2px 2px rgba(0,0,0,.25);
}
.hero-photo{left:23px;top:106px;width:330px;height:307px;background:radial-gradient(ellipse at 55% 40%,#f3d8c1,#d9b296 55%,#efe6df)}
.intro-panel{left:353px;top:106px;width:331px;height:307px;background:var(--slate)}
.question{
  position:absolute;left:9px;width:322px;height:46px;border-radius:23px;background:var(--red);
  display:flex;align-items:center;justify-content:center;font-size:26px;font-weight:300;
}
.question b{color:var(--yellow);font-weight:600}
.q1{top:15px}.q2{top:72px}
.intro-text{position:absolute;left:0;top:140px;width:331px;text-align:center;font-size:19px;font-weight:300;line-height:29px}
.intro-text b{font-weight:600}
.intro-text .big{display:block;color:var(--yellow);font-size:28px;font-weight:600;line-height:30px}
.rule{left:0;top:446px;width:712px;height:3px;background:#5a6069}
.bio-band{left:18px;top:413px;width:674px;height:52px}
.bio-text{left:35px;top:413px;width:639px;height:52px;display:flex;flex-direction:column;justify-content:center;text-align:center;font-size:12.5px;font-weight:300;line-height:21px}
.bio-text b{font-weight:600}
.lead{left:39px;top:478px;font-size:14px;font-weight:600;color:var(--navy-text)}
.topic{position:absolute;top:505px;width:208px;height:215px}
.topic-head{height:44px;background:var(--card-head);border-top:2px solid var(--red);display:flex;align-items:center;justify-content:center;font-family:"Open Sans",sans-serif;font-size:15px;letter-spacing:.6px}
.topic-photo{height:171px}
.t1{left:21px}.t2{left:251px}.t3{left:479px}
.t1 .topic-photo{background:linear-gradient(160deg,#2a3346,#4a4f5e 55%,#201c22)}
.t2 .topic-photo{background:linear-gradient(150deg,#f2f2f2,#b89583 50%,#e8e4e0)}
.t3 .topic-photo{background:linear-gradient(160deg,#eeeeee,#d7b59d 55%,#f5f5f5)}
.profile-band{left:0;top:720px;width:712px;height:47px;background:var(--band-yellow);color:var(--ink);font-size:12px;text-align:center;line-height:15.5px;padding-top:8px}
.profile-band b{font-weight:700}
.info-panel{left:0;top:767px;width:380px;height:177px;background:var(--slate);text-align:center;font-family:"Open Sans",sans-serif}
.info-title{font-family:"Fira Sans Condensed",sans-serif;font-size:24px;font-weight:400;margin-top:4px}
.info-text{font-size:14px;line-height:25px;margin-top:4px}
.info-text .hl{color:var(--yellow);font-weight:700}
.info-text b{font-weight:700}
.brand{left:4px;top:895px;width:374px;height:45px;background:var(--white);display:flex;align-items:center;gap:10px;padding-left:10px}
.brand-dot{width:26px;height:26px;border-radius:50%;background:var(--navy-text)}
.brand-name{font-size:24px;font-weight:700;color:var(--navy-text)}
.offer-panel{left:380px;top:767px;width:332px;height:177px;background:linear-gradient(180deg,var(--red),var(--red-deep))}
.offer-tag{position:absolute;left:4px;top:0;width:30px;height:171px;background:var(--green)}
.offer-tag span{position:absolute;left:50%;top:50%;transform:translate(-50%,-50%) rotate(-90deg);white-space:nowrap;color:var(--ink);font-weight:700;font-size:18px;letter-spacing:1px}
.offer-head{position:absolute;left:44px;top:14px;width:285px;font-size:21px;line-height:32px;font-weight:600;color:var(--yellow);letter-spacing:-.5px}
.offer-head .w{color:var(--white);font-weight:300}
.offer-head .free{color:var(--yellow)}
.offer-head .lite{color:var(--white)}
.offer-body{position:absolute;left:40px;top:100px;width:290px;text-align:center;font-size:15.5px;font-weight:300;line-height:18px}
.cta{left:0;top:944px;width:712px;height:42px}
.cta-text{left:22px;top:944px;height:42px;display:flex;align-items:center;font-family:"Open Sans",sans-serif;font-weight:700;font-size:19px}
.cta-phone{left:478px;top:944px;height:42px;display:flex;align-items:center;gap:4px;font-size:30px;font-weight:600}
</style>
</head>
<body>
<div class="canvas">
  <div class="poster">
    <svg class="abs headline-bubble" viewBox="0 0 712 130" aria-hidden="true">
      <path d="M63 31 H649 A37 37 0 0 1 649 105 H92 L92 125 L62 105 A37 37 0 0 1 63 31 Z" fill="var(--orange)"/>
    </svg>
    <h1 class="abs headline">Are you feeling out of sorts?</h1>

    <div class="abs hero-photo" role="img" aria-label="Photo of a stressed woman holding her head in her hands"></div>
    <div class="abs intro-panel">
      <div class="question q1">Is your&nbsp;<b>body changing ?</b></div>
      <div class="question q2">Could it be your&nbsp;<b>hormones ?</b></div>
      <p class="intro-text">If you’re experiencing <b>changes</b> due to<span class="big">hormonal imbalances,</span>it’s important to consult with a<br><b>qualified medical professional<br>who understands your needs.</b></p>
    </div>

    <div class="abs rule"></div>
    <svg class="abs bio-band" viewBox="0 0 674 52" aria-hidden="true">
      <polygon points="0,34 17,24 17,44" fill="var(--navy-band)"/>
      <polygon points="674,34 657,24 657,44" fill="var(--navy-band)"/>
      <rect x="17" y="0" width="640" height="52" fill="var(--navy-band)"/>
    </svg>
    <p class="abs bio-text"><span><b>Karim Oduya</b>, the <b>vBlendwell Apothecary</b>, can help. He has practiced <b>pharmacy</b> and <b>nutritional medicine</b>,</span><span>helping people with <b>hormone imbalances</b> using a <b>holistic approach</b> for <b>over 18 years</b>.</span></p>

    <p class="abs lead">Together, we look at issues around</p>

    <div class="topic t1"><div class="topic-head">HORMONAL IMBALANCE</div><div class="topic-photo" role="img" aria-label="Photo of a sleepless woman in bed beside an alarm clock"></div></div>
    <div class="topic t2"><div class="topic-head">PERIMENOPAUSE</div><div class="topic-photo" role="img" aria-label="Photo of a woman holding her forehead with a headache"></div></div>
    <div class="topic t3"><div class="topic-head">MENOPAUSE</div><div class="topic-photo" role="img" aria-label="Photo of a woman holding her stomach in discomfort"></div></div>

    <p class="abs profile-band">To start, we take a profile of your <b>sex hormones</b>, <b>Adrenals</b>, <b>Thyroids</b> and <b>Metabolic Pathways</b> to see how we can best remedy<br>the situation. Karim uses a holistic approach that treats you as a whole – not just the symptoms – for overall better wellness.</p>

    <div class="abs info-panel">
      <h2 class="info-title">Want to know more?</h2>
      <p class="info-text"><span class="hl">Karim</span> is available for consultation on <span class="hl">Wednesday<br>Mornings</span> at <b>Fern Gully Pharmacy</b> and<br><span class="hl">Thursday Mornings</span> at <b>Cape Lorne Pharmacy</b>.</p>
    </div>
    <div class="abs brand"><span class="brand-dot"></span><span class="brand-name">vBlendwell Apothecary</span></div>

    <div class="abs offer-panel">
      <div class="offer-tag"><span>SPECIAL OFFER</span></div>
      <p class="offer-head">BOOK FOR 1 SESSION <span class="w">( $60) &amp;</span><br><span class="lite">GET ANOTHER SESSION</span> <span class="free">FREE</span></p>
      <p class="offer-body">This limited-time package includes an initial consultation, historical hormone profile, follow-up consultation and wellness action plan.</p>
    </div>

    <svg class="abs cta" viewBox="0 0 712 42" aria-hidden="true">
      <rect width="712" height="42" fill="var(--orange)"/>
      <polygon points="0,0 456,0 482,42 0,42" fill="var(--black)"/>
    </svg>
    <p class="abs cta-text">To book an appointment with Karim, call today</p>
    <p class="abs cta-phone">
      <svg width="28" height="28" viewBox="0 0 28 28" aria-hidden="true">
        <circle cx="14" cy="14" r="12" fill="none" stroke="var(--red)" stroke-width="2"/>
        <path d="M9 8c1-1 2-1 2.5 0l1.2 2.4c.3.6.1 1.2-.4 1.6l-.8.6c.8 1.7 2 2.9 3.7 3.7l.6-.8c.4-.5 1-.7 1.6-.4l2.4 1.2c1 .5 1 1.5 0 2.5-1.3 1.3-3 1.4-5 .3-3-1.6-5.2-3.8-6.8-6.8-1-2-1-3.7.3-5z" fill="var(--red)"/>
      </svg>1300 482 615</p>
  </div>
</div>
</body>
</html>
```